BRIM Outreach Partners Business Card Rebrand

Hello Designers! We are looking for help designing our new business card to go in conjunction with our company rebrand. Unfortunately, we have an event mid June that requires we get these printed ASAP (before our new website is launched.) We have a mostly complete Brand Book which I have uploaded to this request for your reference to company information, style, fonts. I've also enclosed our logo file in .eps & .jpg. Attached is a sample business card my boss liked but said was "too simple." I made it in Canva and do not profess to be a designer. NOT FOR DESIGN REFERENCE, ONLY FOR CONTEXT Here is what our old website looks like: https://brimoutreachpartners.com/.

```html
<!DOCTYPE html>
<html lang="en">
<head>
<meta charset="utf-8">
<title>BRIM Outreach Partners – Business Card</title>
<link rel="stylesheet" href="https://fonts.googleapis.com/css2?family=Montserrat:wght@400;500;600;700&display=swap">
<style>
  :root {
    --sky: #4fb3e6;
    --ink: #1b1b1b;
    --card-white: #ffffff;
    --card-black: #1a1a1a;
    --backdrop: #3a3a3c;
    --brand-white: #ffffff;
  }
  * { box-sizing: border-box; margin: 0; padding: 0; }
  html, body { width: 1200px; height: 1200px; overflow: hidden; }
  body {
    background: var(--backdrop);
    font-family: "Montserrat", Arial, sans-serif;
    position: relative;
  }
  .card {
    position: absolute;
    left: 180px;
    width: 840px;
    height: 480px;
    border-radius: 30px;
    overflow: hidden;
    box-shadow: 0 4px 0 var(--sky), 0 18px 40px rgba(0,0,0,.45);
  }
  .card--front { top: 90px; background: var(--card-white); }
  .card--back  { top: 630px; background: var(--card-black); }

  .front__accent {
    position: absolute;
    left: 540px;
    top: 50px;
    width: 280px;
    height: 280px;
    border-radius: 50%;
    background: var(--sky);
  }
  .front__details {
    position: absolute;
    left: 64px;
    top: 250px;
    width: 450px;
  }
  .person-name {
    color: var(--sky);
    font-weight: 600;
    font-size: 32px;
    letter-spacing: .4px;
    text-transform: uppercase;
    line-height: 1;
    white-space: nowrap;
  }
  .person-role {
    color: var(--ink);
    font-weight: 500;
    font-size: 18px;
    letter-spacing: .6px;
    text-transform: uppercase;
    margin-top: 8px;
  }
  .contact-list { list-style: none; margin-top: 22px; }
  .contact-list li {
    display: flex;
    align-items: center;
    gap: 12px;
    color: var(--ink);
    font-size: 19px;
    font-weight: 400;
    line-height: 1.65;
    white-space: nowrap;
  }
  .contact-icon { width: 20px; height: 20px; fill: var(--sky); flex: none; }

  .back__brand {
    position: absolute;
    inset: 0;
    display: flex;
    align-items: center;
    justify-content: center;
    gap: 26px;
  }
  .brand-dot {
    width: 120px;
    height: 120px;
    border-radius: 50%;
    background: var(--sky);
    flex: none;
  }
  .brand-name {
    color: var(--brand-white);
    font-weight: 700;
    font-size: 44px;
    line-height: 1.1;
    letter-spacing: .5px;
  }
</style>
</head>
<body>

  <section class="card card--front">
    <div class="front__accent"></div>
    <div class="front__details">
      <h1 class="person-name">Jordan Ellis-Marsh</h1>
      <p class="person-role">Managing Partner</p>
      <ul class="contact-list">
        <li>
          <svg class="contact-icon" viewBox="0 0 24 24" aria-hidden="true"><path d="M6.6 10.8a15.1 15.1 0 0 0 6.6 6.6l2.2-2.2a1 1 0 0 1 1-.25 11.4 11.4 0 0 0 3.6.6 1 1 0 0 1 1 1V20a1 1 0 0 1-1 1A17 17 0 0 1 3 4a1 1 0 0 1 1-1h3.5a1 1 0 0 1 1 1c0 1.25.2 2.45.6 3.6a1 1 0 0 1-.25 1z"/></svg>
          +945-555-0142
        </li>
        <li>
          <svg class="contact-icon" viewBox="0 0 24 24" aria-hidden="true"><path d="M2 5h20v14H2z M2 5l10 8 10-8" fill="none" stroke="#4fb3e6" stroke-width="2"/><path d="M2 5h20l-10 8z"/></svg>
          jordan@brimoutreachpartners.com
        </li>
        <li>
          <svg class="contact-icon" viewBox="0 0 24 24" aria-hidden="true"><path d="M12 2a7 7 0 0 0-7 7c0 5.2 7 13 7 13s7-7.8 7-13a7 7 0 0 0-7-7zm0 9.5a2.5 2.5 0 1 1 0-5 2.5 2.5 0 0 1 0 5z"/></svg>
          Raleigh, NC based (Eastern Time)
        </li>
      </ul>
    </div>
  </section>

  <section class="card card--back">
    <div class="back__brand">
      <span class="brand-dot"></span>
      <span class="brand-name">BRIM Outreach<br>Partners</span>
    </div>
  </section>

</body>
</html>
```